Stationary for a property rental company
Glenbrook Rentals
Stationary for a property rental company - Real Estate
Creative Brief
Simple
Marla Pike
Owner
PO Box 7413 Ashford Falls, VT 05199
marla@glenbrookrentals-example.net
www.glenbrookrentals-example.net
Please use similar colors that are found in the Logo.
Use emblem for the back of the card

```html
<!DOCTYPE html>
<html lang="en">
<head>
<meta charset="utf-8">
<title>Glenbrook Rentals – Business Card</title>
<link rel="stylesheet" href="https://fonts.googleapis.com/css2?family=Cinzel:wght@400;600&display=swap">
<style>
  :root {
    --backdrop: #e4e2df;
    --card: #ffffff;
    --navy: #2d4052;
    --blue: #4a86a6;
    --blue-tab: #3f7c9e;
    --green: #9cbb31;
    --grey: #5d6166;
    --icon: #4a86a6;
  }
  * { margin: 0; padding: 0; box-sizing: border-box; }
  html, body {
    width: 1200px; height: 902px; overflow: hidden;
    background: var(--backdrop);
    font-family: "Cinzel", "Times New Roman", serif;
  }
  .card {
    position: absolute; left: 100px; top: 165px;
    width: 1000px; height: 572px;
    background: var(--card);
    box-shadow: 0 6px 24px rgba(0,0,0,.12);
    overflow: hidden;
  }
  .brand {
    position: absolute; top: 70px; left: 0; width: 100%;
    display: flex; flex-direction: column; align-items: center; gap: 18px;
  }
  .brand-dot {
    width: 58px; height: 58px; border-radius: 50%;
    background: var(--blue);
  }
  .brand-name {
    font-weight: 600; font-size: 46px; letter-spacing: 3px;
    color: var(--navy); text-transform: uppercase; line-height: 1;
  }
  .person {
    position: absolute; top: 222px; left: 0; width: 100%;
    text-align: center;
  }
  .person-name {
    font-size: 28px; color: var(--blue); letter-spacing: 1px;
  }
  .person-role {
    font-size: 20px; color: var(--grey); margin-top: 6px;
  }
  .contacts {
    position: absolute; top: 308px; left: 180px;
    display: grid; grid-template-columns: 350px auto;
    row-gap: 14px; column-gap: 20px;
    font-size: 15px; color: var(--grey);
  }
  .contact { display: flex; align-items: center; gap: 8px; white-space: nowrap; }
  .contact svg { width: 18px; height: 18px; flex: none; }
  .band {
    position: absolute; left: 0; top: 406px; width: 100%; height: 20px;
    background: var(--green);
  }
  .web-tab {
    position: absolute; left: 330px; top: 392px; width: 600px; height: 68px;
    background: var(--blue-tab); border-radius: 10px;
    display: flex; align-items: center; justify-content: center;
    color: #fff; font-size: 22px; letter-spacing: 3px; text-transform: uppercase;
  }
</style>
</head>
<body>
  <main class="card">
    <header class="brand">
      <div class="brand-dot"></div>
      <div class="brand-name">Glenbrook Rentals</div>
    </header>

    <section class="person">
      <div class="person-name">Marla Pike</div>
      <div class="person-role">Owner</div>
    </section>

    <section class="contacts">
      <div class="contact">
        <svg viewBox="0 0 20 20"><circle cx="10" cy="10" r="10" fill="var(--icon)"/><path d="M10 4.5c-2.2 0-3.8 1.6-3.8 3.6 0 2.8 3.8 7.2 3.8 7.2s3.8-4.4 3.8-7.2c0-2-1.6-3.6-3.8-3.6z" fill="#fff"/><circle cx="10" cy="8.2" r="1.4" fill="var(--icon)"/></svg>
        <span>PO Box 7413 Ashford Falls, VT 05199</span>
      </div>
      <div class="contact">
        <svg viewBox="0 0 20 20"><circle cx="10" cy="10" r="10" fill="var(--icon)"/><circle cx="10" cy="10" r="5.5" fill="none" stroke="#fff" stroke-width="1.2"/><ellipse cx="10" cy="10" rx="2.4" ry="5.5" fill="none" stroke="#fff" stroke-width="1.2"/><line x1="4.5" y1="10" x2="15.5" y2="10" stroke="#fff" stroke-width="1.2"/></svg>
        <span>www.glenbrookrentals-example.net</span>
      </div>
      <div class="contact">
        <svg viewBox="0 0 20 20"><circle cx="10" cy="10" r="10" fill="var(--icon)"/><path d="M7 5h2l1 3-1.4 1a7 7 0 0 0 3.4 3.4l1-1.4 3 1v2c0 .6-.5 1-1 1A9 9 0 0 1 6 6c0-.5.4-1 1-1z" fill="#fff"/></svg>
        <span>802-555-0147</span>
      </div>
      <div class="contact">
        <svg viewBox="0 0 20 20"><circle cx="10" cy="10" r="10" fill="var(--icon)"/><rect x="5" y="6.5" width="10" height="7" rx="1" fill="#fff"/><path d="M5.3 7l4.7 3.6L14.7 7" fill="none" stroke="var(--icon)" stroke-width="1"/></svg>
        <span>marla@glenbrookrentals-example.net</span>
      </div>
    </section>

    <div class="band"></div>
    <div class="web-tab">www.glenbrookrentals-example.net</div>
  </main>
</body>
</html>
```